Chiropractic Flyers to be made more up to date

I have used this series of flyers for my own practice. I would like the graphics to be brought up to date and the name of the doctor and the practice, the address, phone number and date to be removed and a blank box inserted in one place on the flyer that other chiropractors could use to personalize the flyers for their practice. On some of the flyers, this information is in several places. I'd like to have it all in one space so that it would be easy for the doctor to add it in their practice. They all need to be bright and colorful with catchy graphics.

```html
<!DOCTYPE html>
<html lang="en">
<head>
<meta charset="utf-8">
<title>Wanted – Holiday Chiropractic Flyer</title>
<link rel="stylesheet" href="https://fonts.googleapis.com/css2?family=Rye&family=Roboto+Condensed:wght@700&display=swap">
<style>
  :root {
    --stage: #f1ece2;
    --wood-dark: #3a1f10;
    --wood-mid: #5a3119;
    --wood-line: #24120a;
    --paper-light: #fff1c9;
    --paper-mid: #f7d68c;
    --paper-edge: #d9913a;
    --ink: #2a170c;
    --accent: #b3261e;
    --accent-soft: rgba(179, 38, 30, 0.08);
    --art-dark: #2e1a0f;
    --art-light: #f2cf86;
  }
  * { box-sizing: border-box; margin: 0; padding: 0; }
  html, body {
    width: 1041px; height: 1200px; overflow: hidden;
    background: var(--stage);
  }
  .flyer {
    position: absolute; left: 75px; top: 20px;
    width: 642px; height: 837px;
    transform: scale(1.386); transform-origin: 0 0;
    background:
      repeating-linear-gradient(180deg, transparent 0 60px, var(--wood-line) 60px 62px),
      linear-gradient(90deg, var(--wood-dark), var(--wood-mid) 30%, var(--wood-dark) 60%, var(--wood-mid) 85%, var(--wood-dark));
    overflow: hidden;
  }
  .parchment { position: absolute; left: 0; top: 0; width: 642px; height: 837px; }
  .headline {
    position: absolute; left: 0; width: 642px; text-align: center;
    font-family: "Rye", serif; font-weight: 400;
    transform-origin: 50% 0;
    white-space: nowrap;
  }
  .headline--wanted {
    top: 94px; font-size: 86px; line-height: 86px;
    color: var(--ink); transform: scaleX(0.62);
  }
  .headline--reward {
    top: 399px; font-size: 68px; line-height: 68px;
    color: var(--accent); transform: scaleX(0.63);
  }
  .outlaw-art {
    position: absolute; left: 193px; top: 174px; width: 281px; height: 224px;
    border: 1.5px solid var(--ink);
    background: radial-gradient(ellipse at 58% 52%, var(--art-dark) 0 36%, var(--art-light) 72%);
  }
  .description {
    position: absolute; left: 121px; top: 481px; width: 402px;
    font-family: "Roboto Condensed", sans-serif; font-weight: 700;
    font-size: 14.6px; line-height: 18px; color: var(--ink);
    text-align: justify;
  }
  .description p + p { margin-top: 4px; }
  .practice-box {
    position: absolute; left: 121px; top: 662px; width: 402px; height: 70px;
    border: 1.5px dashed var(--accent);
    background: var(--accent-soft);
    border-radius: 4px;
  }
  .fine-print {
    position: absolute; left: 121px; top: 748px; width: 420px;
    font-family: "Roboto Condensed", sans-serif; font-weight: 700;
    font-size: 11.4px; line-height: 13px; color: var(--ink);
    text-transform: uppercase; white-space: nowrap;
  }
</style>
</head>
<body>
  <main class="flyer">
    <svg class="parchment" viewBox="0 0 642 837" aria-hidden="true">
      <defs>
        <radialGradient id="paperTone" cx="50%" cy="45%" r="65%">
          <stop offset="0" stop-color="#fff1c9"/>
          <stop offset="0.7" stop-color="#f7d68c"/>
          <stop offset="1" stop-color="#d9913a"/>
        </radialGradient>
      </defs>
      <polygon fill="url(#paperTone)" points="
        60,48 110,44 160,50 220,45 280,49 340,44 400,50 460,46 520,50 575,45 598,52
        592,110 600,170 594,240 601,310 595,380 600,450 593,520 599,590 594,660 600,730 595,770 590,790
        540,787 480,792 420,786 360,791 300,786 240,792 180,787 120,791 70,786 52,788
        47,730 53,660 46,590 52,520 45,450 51,380 46,310 53,240 47,170 52,110 49,60"/>
      <rect x="61" y="62" width="528" height="721" fill="none" stroke="#2a170c" stroke-width="1" opacity="0.6"/>
    </svg>

    <h1 class="headline headline--wanted">WANTED</h1>
    <div class="outlaw-art" role="img" aria-label="Silhouette of an outlaw in a wide-brimmed cowboy hat"></div>
    <h2 class="headline headline--reward">REWARED!</h2>

    <div class="description">
      <p>Desperate person in pain, May look like they have a bad headache, stiff neck, or low back pain. They may even look like they have a lot of pain between the shoulder blades, at the elbow or knee.</p>
      <p>If you see this person please be advised they may be grumpy and in need of chiropractic care. There is a reward of a family-sized turkey for any desperate character brought in fitting the description during the holiday month.</p>
    </div>

    <div class="practice-box" aria-label="Space for practice name, address, phone and dates"></div>

    <p class="fine-print">Offer not valid for Medicare, Workers Comp. or Personal Injury Cases.</p>
  </main>
</body>
</html>
```